Cybersecurity company is looking for business card.

I need a business card design for our company, we are a cybersecurity company providing advance technology to protect agains any kind of malware. We need a fresh modern design it should communicate modern, technology and growth.

Target Market(s)

Business to business

Industry/Entity Type

Business

Contact Information for Business Card

Should have location, address, fax, mobile, phone, email and website.

Requirements
Must have
• Must follow company's logo color and style. Must have the company's log on its.

```html
<!DOCTYPE html>
<html lang="en">
<head>
<meta charset="UTF-8">
<title>Veltrix Business Card</title>
<link rel="stylesheet" href="https://fonts.googleapis.com/css2?family=Roboto:wght@300;400;700&display=swap">
<style>
  :root {
    --stage: #141414;
    --card: #fbfbfb;
    --ink: #111111;
    --text: #3a3a3a;
    --icon: #3d3d3d;
    --accent: #b3191c;
  }
  * { margin: 0; padding: 0; box-sizing: border-box; }
  html, body { width: 1200px; height: 900px; overflow: hidden; background: var(--stage); }
  .stage {
    position: relative; width: 1200px; height: 900px;
    display: flex; flex-direction: column; align-items: center; justify-content: center; gap: 60px;
    font-family: "Roboto", sans-serif;
  }
  .card {
    position: relative; width: 600px; height: 350px; background: var(--card);
  }
  .brand {
    position: absolute; display: flex; align-items: flex-start; gap: 6px;
    font-family: "Roboto", sans-serif; font-weight: 700; color: var(--ink); letter-spacing: 0.5px; line-height: 1;
  }
  .brand-mark { background: var(--accent); flex: none; }
  .card-back .brand { top: 52px; right: 66px; font-size: 46px; }
  .card-back .brand-mark { width: 9px; height: 9px; margin-top: 4px; }
  .card-front .brand { top: 50%; left: 50%; transform: translate(-50%, -50%); font-size: 92px; }
  .card-front .brand-mark { width: 16px; height: 16px; margin-top: 8px; }

  .address { position: absolute; left: 46px; top: 104px; display: flex; gap: 14px; }
  .address svg { width: 14px; height: 22px; margin-top: 1px; }
  .address p { font-weight: 300; font-size: 19px; line-height: 28px; color: var(--text); }

  .contacts { position: absolute; left: 74px; top: 188px; list-style: none; }
  .contacts li { display: flex; align-items: center; gap: 11px; height: 26px; font-weight: 300; font-size: 19px; color: var(--text); }
  .contacts svg { width: 17px; height: 17px; fill: var(--icon); flex: none; }
</style>
</head>
<body>
<main class="stage">
  <section class="card card-back" aria-label="Card back with contact details">
    <div class="brand"><span>veltrix</span><span class="brand-mark"></span></div>
    <div class="address">
      <svg viewBox="0 0 14 22" aria-hidden="true"><path d="M7 0C3.1 0 0 3 0 6.8 0 11.5 7 22 7 22s7-10.5 7-15.2C14 3 10.9 0 7 0z" fill="var(--accent)"/><circle cx="7" cy="6.8" r="2.3" fill="#fff"/></svg>
      <p>location<br>address</p>
    </div>
    <ul class="contacts">
      <li><svg viewBox="0 0 17 17" aria-hidden="true"><rect x="2" y="0.5" width="13" height="16" rx="1.5"/><rect x="4.5" y="4" width="8" height="1.2" fill="#fff"/><rect x="4.5" y="7.5" width="8" height="1.2" fill="#fff"/><rect x="4.5" y="11" width="8" height="1.2" fill="#fff"/></svg>fax</li>
      <li><svg viewBox="0 0 17 17" aria-hidden="true"><rect x="3.5" y="0.5" width="10" height="16" rx="1.8"/><rect x="5.2" y="2.5" width="6.6" height="9.5" fill="#fff"/><circle cx="8.5" cy="14.2" r="1" fill="#fff"/></svg>mobile</li>
      <li><svg viewBox="0 0 17 17" aria-hidden="true"><path d="M3.2 16.5 1 14.8c-.9-.8-.4-2.3.3-3.2C4 7.8 8 4.2 12.6 2.2c1-.4 2.4-.5 3 .5l1 2c.3.7-.2 1.2-.8 1.5l-2.4 1c-.6.2-1.2-.2-1.4-.8l-.3-1c-2.6 1.4-4.8 3.6-6.2 6.3l1 .4c.6.3.9.9.6 1.5l-1.3 2.4c-.4.6-1 .9-1.6.5z"/></svg>phone</li>
      <li><svg viewBox="0 0 17 17" aria-hidden="true"><rect x="0.5" y="3.5" width="16" height="11" rx="1"/><path d="M1.5 4.5 8.5 10l7-5.5" fill="none" stroke="#fff" stroke-width="1.3"/></svg>email</li>
      <li><svg viewBox="0 0 17 17" aria-hidden="true"><circle cx="8.5" cy="8.5" r="8"/><g fill="none" stroke="#fff" stroke-width="0.9"><ellipse cx="8.5" cy="8.5" rx="3.4" ry="8"/><path d="M0.5 8.5h16M8.5 0.5v16M1.8 4.5h13.4M1.8 12.5h13.4"/></g></svg>website</li>
    </ul>
  </section>

  <section class="card card-front" aria-label="Card front with company name">
    <div class="brand"><span>veltrix</span><span class="brand-mark"></span></div>
  </section>
</main>
</body>
</html>
```